Realtor resource

This is a website that provides resources for Realtors and their customers (home buyers and sellers).

There are 5 pages that I need redesigned:

1. Homepage: https://brightkeyguide.example/
2. Support Page/Contact Us: https://brightkeyguide.example/contact-us/
3. Agent Dashboard - See attached screenshot
4. Real Estate Documents page - See attached screenshot
5. Real Estate Contract page - see attached screenshot

Target Market(s)

Real estate agents and their customers.

Industry/Entity Type

Real Estate

Number of Pages Required

5+ page

Requirements
Must have
• Please use a modern design and incorporate design with current logo.

```html
<!DOCTYPE html>
<html lang="en">
<head>
<meta charset="utf-8">
<title>Bright Key Guide – Real Estate Contracts Explained</title>
<link rel="stylesheet" href="https://fonts.googleapis.com/css2?family=Libre+Franklin:wght@300;400;500;600;700&display=swap">
<style>
  :root {
    --orange: #f7931e;
    --page: #f4f4f4;
    --ink: #111111;
    --nav-ink: #222222;
    --white: #ffffff;
    --field-line: #cfcfcf;
    --muted: #8a8a8a;
  }
  * { box-sizing: border-box; margin: 0; padding: 0; }
  html, body { width: 1200px; height: 1080px; overflow: hidden; }
  body {
    position: relative;
    background: var(--page);
    font-family: "Libre Franklin", Arial, sans-serif;
    color: var(--ink);
  }
  .stage { position: absolute; inset: 0; width: 1200px; height: 1080px; }

  .site-header {
    position: absolute; top: 0; left: 0; width: 1200px; height: 96px;
    background: var(--page);
    box-shadow: 0 2px 10px rgba(0,0,0,0.08);
    z-index: 2;
  }
  .brand {
    position: absolute; left: 90px; top: 33px;
    font-size: 25px; font-weight: 600; color: var(--ink); letter-spacing: -0.5px;
    text-decoration: none;
  }
  .main-nav { position: absolute; top: 40px; left: 455px; display: flex; gap: 52px; font-size: 14px; }
  .main-nav a { color: var(--nav-ink); text-decoration: none; font-weight: 500; }
  .main-nav a.is-active { color: var(--orange); }
  .search {
    position: absolute; left: 846px; top: 32px; width: 223px; height: 33px;
    border: 1px solid var(--field-line); border-radius: 17px; background: var(--white);
  }
  .search-field {
    position: absolute; left: 12px; top: 9px;
    font-size: 11px; font-style: italic; color: var(--muted);
  }
  .search-button {
    position: absolute; right: -1px; top: -1px; width: 33px; height: 33px;
    border: 1px solid var(--orange); border-radius: 50%; background: var(--white);
    display: flex; align-items: center; justify-content: center;
  }
  .account-button {
    position: absolute; left: 1077px; top: 31px; width: 34px; height: 34px;
    border-radius: 50%; background: var(--orange);
    display: flex; align-items: center; justify-content: center;
  }

  .hero-title {
    position: absolute; left: 88px; top: 134px;
    font-size: 29px; line-height: 40px; font-weight: 300; color: var(--ink);
  }
  .hero-title strong { font-weight: 600; }
  .scroll-arrow { position: absolute; left: 186px; top: 302px; }

  .audience {
    position: absolute; text-align: center; color: var(--white); width: 400px;
  }
  .audience h2 { font-size: 29px; font-weight: 600; line-height: 1.2; }
  .audience p { font-size: 14px; margin-top: 6px; }
  .btn {
    display: inline-block; margin-top: 30px; height: 34px; padding: 0 22px;
    border-radius: 17px; font-size: 12px; font-weight: 600; line-height: 32px;
    text-decoration: none;
  }
  .btn-outline { border: 1px solid var(--white); color: var(--white); }
  .btn-solid { border: 1px solid var(--white); background: var(--white); color: var(--ink); }
  .audience-realtor { left: 664px; top: 354px; }
  .audience-owners { left: 136px; top: 663px; }

  .site-footer { position: absolute; right: 89px; top: 923px; text-align: right; color: var(--white); }
  .help-row { display: flex; align-items: center; justify-content: flex-end; gap: 15px; font-size: 12px; }
  .help-row .btn { margin-top: 0; padding: 0 29px; }
  .copyright { margin-top: 19px; font-size: 12px; }
  .copyright strong { font-weight: 600; }
</style>
</head>
<body>
  <svg class="stage" viewBox="0 0 1200 1080">
    <defs>
      <linearGradient id="realtorTone" x1="0" y1="0" x2="1" y2="1">
        <stop offset="0" stop-color="#8a7f76"/>
        <stop offset="0.55" stop-color="#5a4e47"/>
        <stop offset="1" stop-color="#2e2a28"/>
      </linearGradient>
      <linearGradient id="ownersTone" x1="0" y1="0" x2="1" y2="1">
        <stop offset="0" stop-color="#4a3c36"/>
        <stop offset="0.5" stop-color="#80604e"/>
        <stop offset="1" stop-color="#5d4e48"/>
      </linearGradient>
    </defs>
    <polygon points="0,987 196,1080 1004,793 1200,884 1200,1080 0,1080" fill="var(--orange)"/>
    <g role="img" aria-label="Photo of a young couple reviewing documents with a realtor">
      <polygon points="194,391 1001,96 1200,207 1200,884 1004,793" fill="url(#realtorTone)"/>
    </g>
    <g role="img" aria-label="Photo of buyers and sellers shaking hands over a signed contract">
      <polygon points="0,295 194,391 1004,793 196,1080 0,987" fill="url(#ownersTone)"/>
    </g>
  </svg>

  <header class="site-header">
    <a class="brand" href="https://brightkeyguide.example/">BrightKeyGuide</a>
    <nav class="main-nav">
      <a class="is-active" href="https://brightkeyguide.example/">Home</a>
      <a href="https://brightkeyguide.example/contact-us/">Support</a>
      <a href="#">Real Estate Documents</a>
    </nav>
    <div class="search">
      <span class="search-field">Search Here ...</span>
      <span class="search-button">
        <svg width="11" height="11" viewBox="0 0 12 12"><circle cx="5" cy="5" r="3.5" fill="none" stroke="#111" stroke-width="1.6"/><line x1="7.6" y1="7.6" x2="10.5" y2="10.5" stroke="#111" stroke-width="1.8" stroke-linecap="round"/></svg>
      </span>
    </div>
    <span class="account-button">
      <svg width="12" height="12" viewBox="0 0 12 12"><circle cx="6" cy="3.6" r="2.4" fill="#fff"/><path d="M1.5 11 C1.5 7.5 10.5 7.5 10.5 11 Z" fill="#fff"/></svg>
    </span>
  </header>

  <h1 class="hero-title">Real Estate Contracts <strong>Explained</strong><br><strong>in plain language</strong>&nbsp; by Texas real estate<br>attorneys.</h1>
  <svg class="scroll-arrow" width="16" height="22" viewBox="0 0 16 22"><line x1="8" y1="1" x2="8" y2="20" stroke="var(--orange)" stroke-width="2"/><polyline points="2,14 8,20 14,14" fill="none" stroke="var(--orange)" stroke-width="2"/></svg>

  <section class="audience audience-realtor">
    <h2>Realtor</h2>
    <p>There are many variations of passages of Lorem</p>
    <a class="btn btn-outline" href="#">Sign Up Now!</a>
  </section>

  <section class="audience audience-owners">
    <h2>Buyers &amp; Sellers</h2>
    <p>There are many variations of passages of Lorem</p>
    <a class="btn btn-solid" href="#">Sign Up Now!</a>
  </section>

  <footer class="site-footer">
    <div class="help-row"><span>Need Help?</span><a class="btn btn-outline" href="https://brightkeyguide.example/contact-us/">Contact Us</a></div>
    <p class="copyright">© 2019 <strong>Bright Key Guide.</strong> All Rights Reserved</p>
  </footer>
</body>
</html>
```